依頼詳細
不動産物件情報の冊子の表紙デザインです。春号らしいイメージと、簡単には捨てられないインパクトのあるデザインをお願いします。
※参考まで前号(冬号)の表紙を添付いたします
会社WEB:http://meridel-works.jp/
※必ずしも、前号のイメージにとらわれる必要はありません
記載項目
タイトル「物件情報 2020 春号」 会社ロゴ:添付参照 10周年記念タイトル:添付参照
希望イメージ
シンプル 複雑
単色 カラフル
暗い 明るい
日常 高級
遊び心 厳粛
未来的 伝統的
女性的 男性的
希望する色
設定なし
納品ファイル
• 高解像度JPG (.jpg)
• イラストレーター形式 (.ai)
補足説明
四半期に一度発行予定ですので、継続して発行して行きます
■ 選んだ理由

最終選考の4案中、一番投票が多かったです。
春の都会をうまく表現したデザインで、表紙にふさわしいと決定しました

■ 提案者全員のお礼・コメント

ご提案いただいた、多数の皆様、誠にありがとうございます。
また、次号の募集にもご参加いただければ幸いです

```html
<!DOCTYPE html>
<html lang="ja">
<head>
<meta charset="UTF-8">
<title>物件情報 2020 春号</title>
<link href="https://fonts.googleapis.com/css2?family=Noto+Sans+JP:wght@400;500;700;900&display=swap" rel="stylesheet">
<style>
  :root {
    --paper: #ffffff;
    --accent: #e63b6f;
    --title-top: #f27aa3;
    --title-bottom: #f7b6cd;
    --subtitle: #7a7a7a;
    --brand: #6b5a3a;
    --brand-dot: #d9a43a;
    --city-haze: #fbeff3;
    --city-rose: #e7b3c6;
    --city-deep: #c987a2;
    --city-mauve: #d6a9c4;
    --city-violet: #c7b3d6;
    --city-silver: #e9e4ea;
    --badge: #c9962e;
    --note: #333333;
  }
  * { margin: 0; padding: 0; box-sizing: border-box; }
  html, body { width: 854px; height: 1200px; overflow: hidden; background: var(--paper); }
  .cover {
    position: relative;
    width: 854px;
    height: 1200px;
    overflow: hidden;
    background: var(--paper);
    font-family: "Noto Sans JP", sans-serif;
  }
  .city-scene {
    position: absolute;
    left: 0; top: 290px;
    width: 854px; height: 910px;
    background:
      linear-gradient(180deg, var(--paper) 0%, rgba(255,255,255,0.6) 8%, rgba(255,255,255,0) 20%, rgba(255,255,255,0) 62%, rgba(255,255,255,0.85) 100%),
      radial-gradient(ellipse 260px 360px at 330px 360px, var(--city-deep) 0%, rgba(201,135,162,0) 100%),
      radial-gradient(ellipse 220px 260px at 640px 520px, var(--city-mauve) 0%, rgba(214,169,196,0) 100%),
      radial-gradient(ellipse 180px 300px at 80px 380px, var(--city-silver) 0%, rgba(233,228,234,0) 100%),
      linear-gradient(90deg, var(--city-silver) 0%, var(--city-rose) 30%, var(--city-haze) 58%, var(--city-rose) 78%, var(--city-violet) 100%);
  }
  .brand {
    position: absolute;
    left: 26px; top: 30px;
    width: 190px;
    display: flex; flex-direction: column; align-items: center; gap: 10px;
  }
  .brand-dot {
    width: 110px; height: 110px; border-radius: 50%;
    background: var(--brand-dot);
  }
  .brand-name {
    font-weight: 700; font-size: 26px; color: var(--brand);
    white-space: nowrap; line-height: 1.2;
  }
  .issue {
    position: absolute;
    right: 30px; top: 18px;
    font-weight: 500; font-size: 56px; color: var(--accent);
    letter-spacing: 2px; line-height: 1;
  }
  .title {
    position: absolute;
    right: 14px; top: 78px;
    font-weight: 900; font-size: 148px; line-height: 1;
    letter-spacing: 4px;
    background: linear-gradient(180deg, var(--title-top), var(--title-bottom));
    -webkit-background-clip: text; background-clip: text;
    color: transparent;
  }
  .tagline {
    position: absolute;
    right: 30px; top: 238px;
    font-weight: 500; font-size: 44px; color: var(--subtitle);
    letter-spacing: 4px;
  }
  .anniversary {
    position: absolute;
    left: 516px; top: 1058px;
    display: flex; align-items: center; gap: 12px;
  }
  .anniversary-badge {
    flex: none;
    width: 100px; height: 100px; border-radius: 50%;
    background: radial-gradient(circle at 40% 35%, #f0cf78, var(--badge) 70%);
  }
  .anniversary-note {
    font-weight: 700; font-size: 14px; line-height: 1.6; color: var(--note);
    white-space: nowrap;
  }
</style>
</head>
<body>
  <main class="cover">
    <div class="city-scene" role="img" aria-label="春の光に包まれたピンクと薄紫の高層ビル街の写真"></div>

    <div class="brand">
      <span class="brand-dot"></span>
      <span class="brand-name">Meridel Works</span>
    </div>

    <p class="issue">2020 春</p>
    <h1 class="title">物件情報</h1>
    <p class="tagline">価値ある情報をあなたへ</p>

    <div class="anniversary">
      <span class="anniversary-badge"></span>
      <p class="anniversary-note">株式会社メリデルワークスは、<br>おかげさまで<br>10周年を迎えました</p>
    </div>
  </main>
</body>
</html>
```